Gala Event Program - Italian

Need a program with the exact same layout/structure as attached. The new theme for the event this year will be: Notte di Stelle Dorate, A Night of Golden Stars. The look that we are going for is Italian garden party. The page sizes should also be the same as previously - 8.5 X 11.

The image sizes relative to pring should remain roughly the same for the individual and group pages.

```html
<!DOCTYPE html>
<html lang="en">
<head>
<meta charset="utf-8">
<title>Executive Board of Directors – Notte di Stelle Dorate</title>
<link href="https://fonts.googleapis.com/css2?family=Roboto:wght@400;700&family=Rochester&family=Pinyon+Script&display=swap" rel="stylesheet">
<style>
  :root {
    --gold: #d49d12;
    --gold-light: #f4d35a;
    --frame: #b77a3a;
    --ink: #111111;
    --paper: #ffffff;
    --leaf: #a9dc6c;
    --leaf-soft: #e4f4c8;
    --crystal: #f3dc8a;
    --blossom: #f4b7c5;
    --blossom-soft: #fbe3e9;
  }
  * { margin: 0; padding: 0; box-sizing: border-box; }
  html, body { width: 928px; height: 1200px; overflow: hidden; background: var(--paper); }
  .page { position: relative; width: 928px; height: 1200px; background: var(--paper); font-family: "Roboto", Arial, sans-serif; color: var(--ink); }
  .frame { position: absolute; left: 0; top: 0; }

  .floral-top, .floral-bottom { position: absolute; opacity: 0.85; }
  .floral-top { left: 12px; top: 44px; width: 326px; height: 262px;
    border-radius: 60% 40% 30% 70% / 40% 45% 55% 60%;
    background: linear-gradient(150deg, var(--leaf-soft) 0%, var(--leaf) 35%, var(--blossom-soft) 55%, var(--crystal) 75%, rgba(255,255,255,0) 100%); }
  .floral-bottom { left: 594px; top: 901px; width: 315px; height: 235px;
    border-radius: 40% 60% 55% 45% / 55% 45% 40% 50%;
    background: linear-gradient(330deg, var(--leaf-soft) 0%, var(--leaf) 30%, var(--blossom) 55%, var(--crystal) 78%, rgba(255,255,255,0) 100%); }
  .blossom { position: absolute; width: 34px; height: 34px; border-radius: 50%;
    background: radial-gradient(circle, var(--blossom) 0 35%, var(--blossom-soft) 65%, rgba(255,255,255,0) 72%); }

  .title { position: absolute; left: 400px; width: 310px; text-align: center; }
  .title-main { top: 74px; font-size: 49px; font-weight: 400; line-height: 1; letter-spacing: 0.3px;
    background: linear-gradient(180deg, var(--gold-light), var(--gold)); -webkit-background-clip: text; background-clip: text; color: transparent; }
  .title-sub { top: 112px; font-family: "Rochester", "Pinyon Script", cursive; font-size: 34px; line-height: 1.1; }
  .section-head { position: absolute; width: 200px; text-align: center; font-family: "Rochester", "Pinyon Script", cursive; font-weight: 400; font-size: 54px; line-height: 1; }
  .rule { position: absolute; height: 2px; background: var(--ink); }
  .rule::before, .rule::after { content: ""; position: absolute; top: -2.5px; width: 7px; height: 7px; border-radius: 50%; background: var(--ink); }
  .rule::before { left: -3px; } .rule::after { right: -3px; }
  .roster { position: absolute; list-style: none; font-size: 20.5px; line-height: 25.3px; }
  .roster.right-align { text-align: right; }
  .roster.roles { font-weight: 700; }
  .page-number { position: absolute; left: 407px; top: 1119px; width: 80px; text-align: center; font-size: 30px; font-weight: 700; color: var(--gold); line-height: 1; }
</style>
</head>
<body>
<main class="page">
  <svg class="frame" width="928" height="1200" viewBox="0 0 928 1200" aria-hidden="true">
    <defs>
      <linearGradient id="frameGold" x1="0" y1="0" x2="0" y2="1">
        <stop offset="0" stop-color="#b77a3a"/>
        <stop offset="0.5" stop-color="#f2cf4a"/>
        <stop offset="1" stop-color="#b77a3a"/>
      </linearGradient>
    </defs>
    <g fill="none" stroke="url(#frameGold)" stroke-width="2">
      <path d="M401 63 H860 V858"/>
      <path d="M401 63 C388 63 385 80 394 88 C402 94 411 86 406 79 C402 74 396 78 399 82"/>
      <path d="M860 858 C860 872 843 876 836 868 C830 860 838 851 845 855 C850 858 847 864 843 863"/>
      <path d="M53 1133 V338 C53 325 70 322 77 330 C83 338 75 347 68 343 C63 340 66 334 70 336"/>
      <path d="M53 1133 H401"/>
      <path d="M492 1133 H520 C532 1133 537 1118 528 1111 C520 1105 512 1113 517 1119 C520 1123 525 1120 524 1117"/>
      <path d="M401 1121 A46 46 0 0 1 493 1121"/>
      <path d="M401 1145 A46 46 0 0 0 493 1145"/>
    </g>
    <g fill="#b77a3a">
      <circle cx="401" cy="1121" r="3"/><circle cx="493" cy="1121" r="3"/>
      <circle cx="401" cy="1145" r="3"/><circle cx="493" cy="1145" r="3"/>
    </g>
  </svg>

  <div class="floral-top" role="img" aria-label="Watercolour garden spray of green leaves, pink blossoms, a rosebud and golden crystals"></div>
  <div class="floral-bottom" role="img" aria-label="Watercolour garden spray of pink flowers, a rosebud, leaves and golden crystals"></div>

  <h1 class="title title-main">EXECUTIVE</h1>
  <p class="title title-sub">Board of Directors</p>

  <h2 class="section-head" style="left:413px; top:250px;">Officer</h2>
  <div class="blossom" style="left:409px; top:298px;" role="img" aria-label="Small pink blossom"></div>
  <div class="rule" style="left:455px; top:314px; width:116px;"></div>
  <div class="blossom" style="left:584px; top:298px;" role="img" aria-label="Small pink blossom"></div>

  <ul class="roster roles right-align" style="right:444px; top:343px;">
    <li>President</li><li>President Elect</li><li>VP Membership</li><li>VP Projects</li>
    <li>Recording Secretary</li><li>Treasurer</li><li>Parliamentarian</li><li>Corresponding Secretary</li>
  </ul>
  <ul class="roster" style="left:517px; top:343px;">
    <li>Elena Bartoli</li><li>Laura Bennett</li><li>Chiara Donnelly</li><li>Bianca Varela</li>
    <li>Bethany Marsh</li><li>Hannah Doyle</li><li>Holly Brandt</li><li>Julianne Morrow</li>
  </ul>

  <h2 class="section-head" style="left:405px; top:604px;">Patron</h2>
  <div class="blossom" style="left:399px; top:645px;" role="img" aria-label="Small pink blossom"></div>
  <div class="rule" style="left:446px; top:661px; width:116px;"></div>
  <div class="blossom" style="left:575px; top:645px;" role="img" aria-label="Small pink blossom"></div>

  <ul class="roster right-align" style="right:447px; top:694px;">
    <li>Diana Avery</li><li>Delia Carrington</li><li>Rosalie Garner</li><li>Celia Hartley</li>
    <li>Caterina Kemp</li><li>Serena Lockwood</li><li>Clara Moreno</li>
  </ul>
  <ul class="roster" style="left:517px; top:694px;">
    <li>Dora L. Marlowe</li><li>Carmen Pryor</li><li>Lia Rowland</li><li>Beatrice Sloan</li>
    <li>Brenna Whitfield</li><li>Anna Vance</li>
  </ul>

  <p class="page-number">03</p>
</main>
</body>
</html>
```